Wine Bottle Label for Tall Fern Cellars

We are a small, newly established winery in need of an original, bold and outstanding bottle label design for our Tall Fern wine.

Our vineyard and winery are located on a 200 acre farm in a remote part of southern Oregon. The name "Tall Fern" was inspired by the large, overgrown size of all of the foliage here, including our grapevines. Things grow large and vigorous in Oregon! And everything is very lush and green. It is almost surreal or other-worldly, like the landscapes seen in the Keeper of The Hollows movies, or the land of Yarrowmere. It is a place that makes you say "wow" with its epic, large scale, natural beauty.

The name "Tall Fern" also captures the essence of our wine. It is big in flavor, quality and color. Our first release is a Pinot Noir (red). Pinot Noir wines often are subtle in flavor and thin in their color. Our label should convey that our Pinot Noir is a much more robust, darker, heavier, meatier, more flavorful wine that is a lot more fun than an "ordinary" wine. At the same time, this wine is not cheap, and so nothing in the label should convey "bargain," "low price," or "cheapness." This is a fine wine with a sense of adventure. Be sure to convey "quality" with your design along with "big," "adventure" and "fun".

The label should appeal to a younger demographic, both male and female, between the ages of 21 and 35. It should be non-traditional and adventurous and suggest a pushing of boundaries and a breaking of rules. This Pinot Noir does not conform to the normal "limitations" of the variety, therefore the label should not conform. It should have an "organic" or "natural" or "agricultural" vibe, as opposed to something mechanical or technical. It should, however, be contemporary. Do not confuse "natural" or "organic" with being nostalgic or old school. Think "agri-hipsters."

The label should be designed to fit on a Burgundy-style wine bottle (photo attached for reference). (Note: All Pinot Noir and Chardonnay is bottled in Burgundy bottles, If you are not sure about the bottle shape you can go to a local store and compare the various bottles. Locate a bottle of Pinot Noir or Chardonnay or anything identified as a "Burgundy Wine," and it should be the correct bottle. The tall, skinny bottles used for Cabernet Sauvignon are NOT correct)). Please see the "Must Have" notes for more on the bottle.

In summary, the final project should be a wine bottle label design that conveys bigness, vastness, adventurous, non-traditional, high quality wine. A good tagline to keep in mind is "Living Large."

Target Market(s)

Young, hip, non-conformist wine drinkers aged 21-35 with a sense of adventure and an appreciation of quality.

Industry/Entity Type

School

Requirements
Must have
• *Must contain the words:

Tall Fern (the brand)
2013 Pinot Noir (the vintage year and variety)

*The label must be designed to fit a Burgundy-style wine bottle. A photo is attached for reference.

*Additionally, the label needs to fit on the lower, widest part of the bottle. The label will be printed on sticky paper and rolled onto the bottle with a machine. The machine cannot apply labels to the neck of the bottle. The maximum size of a label that will fit this space is 5.5 inches wide by 4.5 inches tall. You DO NOT have to fill ALL of this space or confine the label shape to a rectangle, but the label cannot exceed this size or it won't stick to the bottle properly. It will really help if you can put your hands on an actual bottle to see the logistics of applying the label. But if that is not possible, just do your best with the instructions you have. I am confident the winning design could be adjusted to fit the bottle, if necessary
Nice to have
• *Wine grape leaf or leaves.

*A concept I have been playing with is sunlight shining through leaves like light through a Kessler lamp or a stained glass window. This is NOT a requirement for this label. However, if the concept inspires and idea, I would be most happy to see it.
Should not have
• IF a leaf or leaves are included in the design (not a requirement) they MUST be wine grapevine leafs and preferably leaves of the Pinot Noir vine. Do not use generic leaves or identifiable leaves such as oak leaves, maple leaves, or anything that looks like the Canadian flag or the Dunmore Ice Hawks hockey logo. Reference the attached photos of wine grape leaves to see the correct leaf type. I am happy to email more photos upon request. These photos may be used in whole or in part in your design, however, a leaf from a photo is NOT a requirement, nor is the image of a leaf or leaves.

This label should NOT be designed for Bordeaux-style wine bottles (the tall, skinny ones).

```html
<!DOCTYPE html>
<html lang="en">
<head>
<meta charset="utf-8">
<title>Tall Fern Cellars – Pinot Noir Label Concepts</title>
<link rel="stylesheet" href="https://fonts.googleapis.com/css2?family=Barlow:wght@400;500;600&family=Open+Sans:wght@400;700&display=swap">
<style>
  :root {
    --board: #000000;
    --caption: #ffffff;
    --mint: #eaf5e8;
    --gold: #c9a433;
    --red: #f0443e;
    --blue: #3a5fc9;
    --teal: #27ae95;
    --plum: #3b1642;
    --ink-dark: #1e1e1e;
    --ink-light: #ffffff;
    --leaf-black: #0c0c0c;
  }
  * { box-sizing: border-box; margin: 0; padding: 0; }
  html, body { width: 1000px; height: 1200px; overflow: hidden; background: var(--board); }
  .board { position: relative; width: 1000px; height: 1200px; background: var(--board); font-family: "Barlow", sans-serif; }

  .front, .back { position: absolute; overflow: hidden; background: var(--label-bg); color: var(--label-ink); }
  .front { width: 200px; height: 289px; }
  .back { width: 203px; height: 189px; }

  .front .artwork {
    position: absolute; left: 0; top: 0; width: 200px; height: 205px;
    background: radial-gradient(ellipse 62% 58% at 50% 50%, var(--leaf) 0 70%, transparent 100%),
                linear-gradient(180deg, var(--splash-a), var(--splash-b) 55%, var(--label-bg));
  }
  .front .brand-name {
    position: absolute; left: 0; right: 0; top: 96px; text-align: center;
    font-weight: 500; font-size: 24px; letter-spacing: 3px; line-height: 1;
    color: var(--brand-ink); text-transform: uppercase;
  }
  .front .wine-name { position: absolute; left: 0; right: 0; top: 220px; text-align: center; font-size: 19px; font-weight: 500; letter-spacing: 1.5px; line-height: 1; }
  .front .vintage { position: absolute; left: 0; right: 0; top: 244px; text-align: center; font-size: 11px; letter-spacing: 3px; line-height: 1; }
  .front .origin { position: absolute; left: 0; right: 0; top: 260px; text-align: center; font-size: 10.5px; font-weight: 500; letter-spacing: 3px; line-height: 1; }

  .back .brand-box {
    position: absolute; left: var(--box-x); top: var(--box-y); width: 50px; height: var(--box-h);
    background: var(--box-bg); color: var(--box-ink);
    display: flex; align-items: flex-end; justify-content: center; padding-bottom: 12px;
    font-size: 9px; font-weight: 600; letter-spacing: 1px; text-transform: uppercase; text-align: center; line-height: 1.1;
  }
  .back .copy { position: absolute; left: var(--copy-x); top: 40px; width: 118px; font-family: "Open Sans", sans-serif; font-size: 5.4px; line-height: 1.35; }
  .back .copy p { margin-bottom: 4px; }
  .back .copy .variety { font-family: "Barlow", sans-serif; font-size: 8.5px; font-weight: 500; letter-spacing: 0.3px; margin: 6px 0 5px; }
  .back .copy .lot { font-size: 6px; margin-top: 6px; }
  .back .copy .volume { font-family: "Barlow", sans-serif; font-size: 8px; margin-top: 4px; display: flex; gap: 22px; }

  .theme-mint  { --label-bg: var(--mint); --label-ink: var(--ink-dark); --leaf: var(--leaf-black); --brand-ink: var(--ink-light); --splash-a: #e9559e; --splash-b: #f0b6cf; --box-bg: var(--leaf-black); --box-ink: var(--ink-light); --box-x: 14px; --box-y: 0px; --box-h: 88px; --copy-x: 76px; }
  .theme-red   { --label-bg: var(--red); --label-ink: var(--ink-dark); --leaf: var(--leaf-black); --brand-ink: var(--ink-light); --splash-a: #e6a12c; --splash-b: #b7c03c; --box-bg: var(--leaf-black); --box-ink: var(--ink-light); --box-x: 14px; --box-y: 0px; --box-h: 88px; --copy-x: 76px; }
  .theme-teal  { --label-bg: var(--teal); --label-ink: var(--ink-dark); --leaf: var(--leaf-black); --brand-ink: var(--ink-light); --splash-a: #d9b12f; --splash-b: #7fb552; --box-bg: var(--leaf-black); --box-ink: var(--ink-light); --box-x: 14px; --box-y: 0px; --box-h: 88px; --copy-x: 76px; }
  .theme-gold  { --label-bg: var(--gold); --label-ink: var(--ink-dark); --leaf: var(--leaf-black); --brand-ink: var(--ink-light); --splash-a: #d8c640; --splash-b: #8f78a4; --box-bg: var(--leaf-black); --box-ink: var(--ink-light); --box-x: 12px; --box-y: 30px; --box-h: 56px; --copy-x: 81px; }
  .theme-blue  { --label-bg: var(--blue); --label-ink: var(--ink-light); --leaf: var(--leaf-black); --brand-ink: var(--ink-light); --splash-a: #c8304f; --splash-b: #6a4fb0; --box-bg: var(--leaf-black); --box-ink: var(--ink-light); --box-x: 12px; --box-y: 30px; --box-h: 56px; --copy-x: 81px; }
  .theme-plum  { --label-bg: var(--plum); --label-ink: var(--ink-light); --leaf: #ffffff; --brand-ink: var(--plum); --splash-a: #a86a2c; --splash-b: #6b2d58; --box-bg: #ffffff; --box-ink: var(--plum); --box-x: 12px; --box-y: 30px; --box-h: 56px; --copy-x: 81px; }

  .option-caption { position: absolute; top: 1096px; width: 200px; text-align: center; font-family: "Open Sans", sans-serif; font-weight: 700; font-size: 13px; color: var(--caption); }
  .client-line { position: absolute; left: 42px; top: 1156px; font-family: "Open Sans", sans-serif; font-weight: 700; font-size: 13px; color: var(--caption); white-space: pre; }
</style>
</head>
<body>
<main class="board">

  <!-- Option 1: square -->
  <section class="front theme-mint" style="left:66px;top:113px">
    <div class="artwork" role="img" aria-label="Painted vine leaf silhouette under pink and magenta paint splashes"></div>
    <div class="brand-name">Tall Fern</div>
    <div class="wine-name">PINOT NOIR</div><div class="vintage">2013</div><div class="origin">OREGON USA</div>
  </section>
  <section class="back theme-mint" style="left:276px;top:217px">
    <div class="brand-box">Tall<br>Fern</div>
    <div class="copy">
      <p>Tall Fern are a producer of premium wine. Tall Fern's Pinot Noir exhibits red berry and ripe black cherry flavors. Sourced from from a vineyard in Oregon, this win typifies the elegance and complexity we strive for.</p>
      <p class="variety">PINOT NOIR 2013</p>
      <p>Produced by Tall Fern Ltd.<br>Tall Fern Road, Oregon, USA.<br>www.tallferncellars.net</p>
      <p>Egg products have been used to purify this wine, in accordance with traditional winemaking techniques. Traces may remain. Contains approx. 8.1 standard drinks. Contains Sulphites.</p>
      <p class="lot">L1105</p>
      <p class="volume"><span>13.5% vol</span><span>750ML e</span></p>
    </div>
  </section>

  <section class="front theme-red" style="left:66px;top:453px">
    <div class="artwork" role="img" aria-label="Painted vine leaf silhouette under orange, yellow and green paint splashes"></div>
    <div class="brand-name">Tall Fern</div>
    <div class="wine-name">PINOT NOIR</div><div class="vintage">2013</div><div class="origin">OREGON USA</div>
  </section>
  <section class="back theme-red" style="left:276px;top:557px">
    <div class="brand-box">Tall<br>Fern</div>
    <div class="copy">
      <p>Tall Fern are a producer of premium wine. Tall Fern's Pinot Noir exhibits red berry and ripe black cherry flavors. Sourced from from a vineyard in Oregon, this win typifies the elegance and complexity we strive for.</p>
      <p class="variety">PINOT NOIR 2013</p>
      <p>Produced by Tall Fern Ltd.<br>Tall Fern Road, Oregon, USA.<br>www.tallferncellars.net</p>
      <p>Egg products have been used to purify this wine, in accordance with traditional winemaking techniques. Traces may remain. Contains approx. 8.1 standard drinks. Contains Sulphites.</p>
      <p class="lot">L1105</p>
      <p class="volume"><span>13.5% vol</span><span>750ML e</span></p>
    </div>
  </section>

  <section class="front theme-teal" style="left:66px;top:790px">
    <div class="artwork" role="img" aria-label="Painted vine leaf silhouette under yellow, green and violet paint splashes"></div>
    <div class="brand-name">Tall Fern</div>
    <div class="wine-name">PINOT NOIR</div><div class="vintage">2013</div><div class="origin">OREGON USA</div>
  </section>
  <section class="back theme-teal" style="left:276px;top:893px">
    <div class="brand-box">Tall<br>Fern</div>
    <div class="copy">
      <p>Tall Fern are a producer of premium wine. Tall Fern's Pinot Noir exhibits red berry and ripe black cherry flavors. Sourced from from a vineyard in Oregon, this win typifies the elegance and complexity we strive for.</p>
      <p class="variety">PINOT NOIR 2013</p>
      <p>Produced by Tall Fern Ltd.<br>Tall Fern Road, Oregon, USA.<br>www.tallferncellars.net</p>
      <p>Egg products have been used to purify this wine, in accordance with traditional winemaking techniques. Traces may remain. Contains approx. 8.1 standard drinks. Contains Sulphites.</p>
      <p class="lot">L1105</p>
      <p class="volume"><span>13.5% vol</span><span>750ML e</span></p>
    </div>
  </section>

  <!-- Option 2: curve -->
  <section class="front theme-gold" style="left:519px;top:110px">
    <div class="artwork" role="img" aria-label="Painted vine leaf silhouette under yellow and lilac paint splashes"></div>
    <div class="brand-name">Tall Fern</div>
    <div class="wine-name">PINOT NOIR</div><div class="vintage">2013</div><div class="origin">OREGON USA</div>
  </section>
  <section class="back theme-gold" style="left:733px;top:214px">
    <div class="brand-box">Tall<br>Fern</div>
    <div class="copy">
      <p>Tall Fern are a producer of premium wine. Tall Fern's Pinot Noir exhibits red berry and ripe black cherry flavors. Sourced from from a vineyard in Oregon, this win typifies the elegance and complexity we strive for.</p>
      <p class="variety">PINOT NOIR 2013</p>
      <p>Produced by Tall Fern Ltd.<br>Tall Fern Road, Oregon, USA.<br>www.tallferncellars.net</p>
      <p>Egg products have been used to purify this wine, in accordance with traditional winemaking techniques. Traces may remain. Contains approx. 8.1 standard drinks. Contains Sulphites.</p>
      <p class="lot">L1105</p>
      <p class="volume"><span>13.5% vol</span><span>750ML e</span></p>
    </div>
  </section>

  <section class="front theme-blue" style="left:519px;top:449px">
    <div class="artwork" role="img" aria-label="Painted vine leaf silhouette under red and violet paint splashes"></div>
    <div class="brand-name">Tall Fern</div>
    <div class="wine-name">PINOT NOIR</div><div class="vintage">2013</div><div class="origin">OREGON USA</div>
  </section>
  <section class="back theme-blue" style="left:733px;top:553px">
    <div class="brand-box">Tall<br>Fern</div>
    <div class="copy">
      <p>Tall Fern are a producer of premium wine. Tall Fern's Pinot Noir exhibits red berry and ripe black cherry flavors. Sourced from from a vineyard in Oregon, this win typifies the elegance and complexity we strive for.</p>
      <p class="variety">PINOT NOIR 2013</p>
      <p>Produced by Tall Fern Ltd.<br>Tall Fern Road, Oregon, USA.<br>www.tallferncellars.net</p>
      <p>Egg products have been used to purify this wine, in accordance with traditional winemaking techniques. Traces may remain. Contains approx. 8.1 standard drinks. Contains Sulphites.</p>
      <p class="lot">L1105</p>
      <p class="volume"><span>13.5% vol</span><span>750ML e</span></p>
    </div>
  </section>

  <section class="front theme-plum" style="left:519px;top:786px">
    <div class="artwork" role="img" aria-label="White vine leaf silhouette under amber and plum paint splashes"></div>
    <div class="brand-name">Tall Fern</div>
    <div class="wine-name">PINOT NOIR</div><div class="vintage">2013</div><div class="origin">OREGON USA</div>
  </section>
  <section class="back theme-plum" style="left:733px;top:890px">
    <div class="brand-box">Tall<br>Fern</div>
    <div class="copy">
      <p>Tall Fern are a producer of premium wine. Tall Fern's Pinot Noir exhibits red berry and ripe black cherry flavors. Sourced from from a vineyard in Oregon, this win typifies the elegance and complexity we strive for.</p>
      <p class="variety">PINOT NOIR 2013</p>
      <p>Produced by Tall Fern Ltd.<br>Tall Fern Road, Oregon, USA.<br>www.tallferncellars.net</p>
      <p>Egg products have been used to purify this wine, in accordance with traditional winemaking techniques. Traces may remain. Contains approx. 8.1 standard drinks. Contains Sulphites.</p>
      <p class="lot">L1105</p>
      <p class="volume"><span>13.5% vol</span><span>750ML e</span></p>
    </div>
  </section>

  <p class="option-caption" style="left:172px">Opt #1- Square</p>
  <p class="option-caption" style="left:627px">Opt #2- Curve</p>
  <p class="client-line">Client: Tall Fern  Wine Label: Brand + Concept Label</p>
</main>
</body>
</html>
```